Book Cover

Book cover for a study guide on Galatians. The title would be: "Unbound Hearts: Called Out to Walk Open" Possibly using a bird breaking free from a cage.+

Target Market(s)

We will sell them to our church.

Requirements
Must have
• Authors are Dr. Martin Oskerby and Dr. Helen Oskerby

```html
<!DOCTYPE html>
<html lang="en">
<head>
<meta charset="utf-8">
<title>Unbound Hearts – Book Cover Wrap</title>
<link href="https://fonts.googleapis.com/css2?family=Crimson+Text:wght@400;600&display=swap" rel="stylesheet">
<style>
  :root {
    --ink: #24262b;
    --paper: #ffffff;
    --band: rgba(214, 190, 140, 0.55);
    --rule: rgba(40, 40, 40, 0.7);
    --sky-top: #c9d8d2;
    --sky-mid: #efe7cc;
    --horizon: #8e9d9a;
    --land: #a9a27a;
    --forest: #6f7d45;
    --water: #4f5a55;
  }
  html, body {
    margin: 0;
    padding: 0;
    width: 1200px;
    height: 675px;
    overflow: hidden;
    background: #ffffff;
  }
  .cover-wrap {
    position: relative;
    width: 1200px;
    height: 675px;
    overflow: hidden;
    font-family: "Crimson Text", Georgia, serif;
  }
  .scene {
    position: absolute;
    inset: 0;
    width: 1200px;
    height: 675px;
  }
  .title-band {
    position: absolute;
    left: 0;
    top: 369px;
    width: 1200px;
    height: 105px;
    background: var(--band);
    border-top: 1px solid var(--rule);
    border-bottom: 1px solid var(--rule);
  }
  .title-band::after {
    content: "";
    position: absolute;
    left: 0;
    right: 0;
    bottom: -6px;
    border-bottom: 1px solid var(--rule);
  }
  .fold {
    position: absolute;
    top: 0;
    width: 1px;
    height: 675px;
    background: var(--rule);
  }
  .fold--left { left: 567px; }
  .fold--right { left: 634px; }

  .front-title {
    position: absolute;
    left: 634px;
    width: 560px;
    top: 366px;
    text-align: center;
    color: var(--ink);
    font-size: 52px;
    letter-spacing: 4px;
    line-height: 1;
    margin: 0;
    font-weight: 400;
  }
  .front-subtitle {
    position: absolute;
    left: 634px;
    width: 560px;
    top: 441px;
    text-align: center;
    color: var(--ink);
    font-size: 21px;
    letter-spacing: 1.5px;
    line-height: 1;
    margin: 0;
  }
  .front-authors {
    position: absolute;
    left: 660px;
    width: 540px;
    top: 556px;
    text-align: center;
    color: var(--paper);
    font-size: 38px;
    letter-spacing: 2px;
    line-height: 36px;
    margin: 0;
  }

  .spine-text {
    position: absolute;
    writing-mode: vertical-rl;
    white-space: nowrap;
    margin: 0;
    line-height: 1;
  }
  .spine-title {
    left: 595px;
    top: 44px;
    font-size: 22px;
    letter-spacing: 1.5px;
    color: var(--ink);
  }
  .spine-subtitle {
    left: 582px;
    top: 44px;
    font-size: 11px;
    letter-spacing: 0.5px;
    color: var(--ink);
  }
  .spine-author {
    font-size: 12px;
    color: var(--paper);
    top: 516px;
  }
  .spine-author--first { left: 604px; }
  .spine-author--second { left: 592px; }
</style>
</head>
<body>
  <div class="cover-wrap">
    <svg class="scene" viewBox="0 0 1200 675" role="img" aria-label="Photograph of a wide sky over distant mountains and a fjord, with a rocky cliff ledge on the right where a small bird flies out of an open golden birdcage">
      <defs>
        <linearGradient id="landscape" x1="0" y1="0" x2="0" y2="1">
          <stop offset="0" stop-color="#bcd1cd"/>
          <stop offset="0.25" stop-color="#ebe4c9"/>
          <stop offset="0.46" stop-color="#f1ead0"/>
          <stop offset="0.52" stop-color="#8e9d9a"/>
          <stop offset="0.62" stop-color="#b7ad86"/>
          <stop offset="0.76" stop-color="#8a9256"/>
          <stop offset="0.86" stop-color="#6f7d45"/>
          <stop offset="0.9" stop-color="#55605a"/>
          <stop offset="1" stop-color="#474c49"/>
        </linearGradient>
      </defs>
      <rect width="1200" height="675" fill="url(#landscape)"/>
    </svg>

    <div class="title-band"></div>
    <div class="fold fold--left"></div>
    <div class="fold fold--right"></div>

    <p class="spine-text spine-title">Unbound Hearts</p>
    <p class="spine-text spine-subtitle">Called Out to Walk Open</p>
    <p class="spine-text spine-author spine-author--first">Dr. Martin Oskerby</p>
    <p class="spine-text spine-author spine-author--second">&amp; Dr. Helen Oskerby</p>

    <h1 class="front-title">Unbound Hearts</h1>
    <p class="front-subtitle">Called Out to Walk Open</p>
    <p class="front-authors">Dr. Martin Oskerby<br>&amp; Dr. Helen Oskerby</p>
  </div>
</body>
</html>
```